Business card design needed

We are a Landscape business based in Sydney. We are targeting upper class clients that have the money to spend on their gardens.
We design, construct and maintain the gardens that we create.
We are looking for modern business card with our logo on it and the colours green grey\black/white scale. The design should communicate modern creative gardens. it should look classy and have a professional feel to it not cheap.should be two sides to the business card. Back side to have the words design construct maintain with possible the vine attached somewhere.
Updates

Project Deadline Extended
Reason: Hi Guys. Some of you have asked for a vector version of the vine so I just need some more time to find it as I don't have it here on my computer. Keep up the good work! Thanks Jon

Hi guys and girls.
You have all done a really good job so far. I have recently uploaded the vector for the vine and the logo as promissed. Looking forward to seeing you use them in your designs. Also i would like to see the words design-construct-maintain on the card as an option maybe on the back.
Thanks .

Target Market(s)

white collar, higher education, high social group in affluent areas

Industry/Entity Type

Business

Contact Information for Business Card

Bright Meadow Landscapes
Jonathan Perrow- 0431 592 740 Director( only need one name and number per card i.e. same design twice with different number and name.)
Paul tremaine- 0417 365 209 Director
www.bmlandscapes.example.au
ABN-872 310 954
Lic- 618094K

Requirements
Must have
• Logo which I am trying to upload but it is not working. I have contacted sketch forge to try and fix this.
Should not have
• Two s

```html
<!DOCTYPE html>
<html lang="en">
<head>
<meta charset="utf-8">
<title>Bright Meadow Landscapes – Business Cards</title>
<link rel="stylesheet" href="https://fonts.googleapis.com/css2?family=Arimo:wght@400;700&display=swap">
<style>
  :root {
    --backdrop: #d9d9d6;
    --card-black: #0b0b0b;
    --card-white: #ffffff;
    --leaf-green: #9fd23a;
    --band-grey: #5a5a5a;
    --vine-grey: #4a4a4a;
    --text-light: #f2f2f2;
    --text-dark: #141414;
  }
  * { margin: 0; padding: 0; box-sizing: border-box; }
  html, body {
    width: 1200px; height: 900px; overflow: hidden;
    background: var(--backdrop);
    font-family: "Arimo", Arial, sans-serif;
  }
  .canvas { position: relative; width: 1200px; height: 900px; }
  .card {
    position: absolute; left: 340px; width: 520px; height: 317px;
    border-radius: 16px; overflow: hidden;
    box-shadow: 0 8px 24px rgba(0,0,0,.25);
  }
  .card--services { top: 105px; background: var(--card-black); }
  .card--contact { top: 478px; background: var(--card-white); }

  .brand-name {
    position: absolute; left: 30px; top: 38px;
    font-size: 30px; font-weight: 700; letter-spacing: .5px;
  }
  .card--services .brand-name { color: var(--text-light); }
  .card--contact .brand-name { color: var(--text-dark); left: 100px; top: 48px; }

  .vine-area {
    position: absolute; right: 0; top: 70px; width: 230px; height: 247px;
    background: radial-gradient(ellipse at 70% 55%, rgba(110,110,110,.55), rgba(60,60,60,.25) 55%, rgba(11,11,11,0) 75%);
  }
  .service-list {
    position: absolute; left: 30px; top: 178px;
    list-style: none; color: var(--leaf-green);
    font-size: 16px; line-height: 20px;
  }
  .service-list li::before {
    content: ""; display: inline-block; width: 6px; height: 6px;
    border-radius: 50%; background: var(--leaf-green);
    margin-right: 10px; vertical-align: middle;
  }

  .wave { position: absolute; left: 0; top: 0; width: 520px; height: 317px; }
  .contact-block { position: absolute; left: 30px; top: 172px; color: var(--text-light); }
  .contact-name { color: var(--leaf-green); font-size: 21px; }
  .contact-role { font-size: 13px; margin-bottom: 10px; color: var(--leaf-green); }
  .contact-line { font-size: 14px; line-height: 19px; }
  .contact-line .label { color: var(--leaf-green); display: inline-block; width: 20px; }
  .registration {
    position: absolute; right: 28px; bottom: 26px;
    color: var(--leaf-green); font-size: 15px; line-height: 19px;
  }
</style>
</head>
<body>
<main class="canvas">
  <section class="card card--services">
    <div class="brand-name">Bright Meadow Landscapes</div>
    <div class="vine-area" role="img" aria-label="Decorative grey vine with leaves"></div>
    <ul class="service-list">
      <li>Turf</li>
      <li>Paving</li>
      <li>Timber/Decks</li>
      <li>Water Features</li>
      <li>Stone/Slate/Sandstone</li>
      <li>Horticultural Concept &amp; Design</li>
    </ul>
  </section>

  <section class="card card--contact">
    <svg class="wave" viewBox="0 0 520 317" aria-hidden="true">
      <path d="M0,140 C170,118 320,140 520,198 L520,317 L0,317 Z" fill="var(--band-grey)"/>
      <path d="M0,156 C180,138 330,160 520,214 L520,317 L0,317 Z" fill="var(--card-black)"/>
    </svg>
    <div class="brand-name">Bright Meadow Landscapes</div>
    <div class="contact-block">
      <div class="contact-name">Jonathan Perrow</div>
      <div class="contact-role">Director</div>
      <div class="contact-line"><span class="label">P:</span>0431 592 740</div>
      <div class="contact-line"><span class="label">E:</span>bmlandscapes@mailbox.example.au</div>
      <div class="contact-line"><span class="label">W:</span>www.bmlandscapes.example.au</div>
    </div>
    <div class="registration">
      <div>ABN: 872 310 954</div>
      <div>Lic:&nbsp;&nbsp;&nbsp;618094K</div>
    </div>
  </section>
</main>
</body>
</html>
```